Business Card & Logo Design - Hedge Fund

We need a business card and logo design for a hedge fund. The hedge fund is named Morvane Equity LLC. Morvane Equity was created by finance professors and the strategy is based academic research that looks for patterns in stock prices. The design should look conservative, solid, strong. We favor a classic style - nothing flashy. The logo can relate to the name Morvane Equity, or it could involve a symbol design that connotes "science" . We are open to ideas. We do not want alot of colors - but if any, color - blue is preferred. The font that seems to look best for the name (Morvane Equity) is arial black. We are open to ideas. Most important - we want to see a mock up of an actual business card with the logo concept embedded. The business card should include space for : company name, individual name, position title, cell phone, address. We hope to have this work done by Sept. 8.

Target Market(s)

We will be meeting with and giving the business card to institutions and high net worth individuals.

Industry/Entity Type

Investment Advisory

Contact Information for Business Card

Company name - Morvane Equity LLC
Individual name - Peter Dalby
Title - Portfolio Manager
Cell - (412) 555-0187
Address - 2650 Birchmont Lane, Suite 300, Atlanta GA 30327

Font styles to use
Other font styles liked:
• Arial

Colors
3277b5
0255a3
85acd3
cedeed
fdf9cf
d9d9d9
e6e6e6
f04a50
6b449b

Requirements
Must have
• Must have card details that are sited above.
• We would like a logo related to the name (Morvane Equity) or concept of the fund.
Nice to have
• We want conservative / understated / clean crisp look.
• If any colors - we prefer conservative appearance - blue / gray.
• I have enclosed an example of a card style that looks attractive - please do not exactly copy this card. This is not our company or logo. I feel the layout is attractive - just as an example
Should not have
• Avoid too much color.
• I have selected some preferred colors. Please do not use all of the colors - I have selected a few that might work - but I am not sure. We are open to your ideas so please do not feel the need to use all or any of these.

```html
<!DOCTYPE html>
<html lang="en">
<head>
<meta charset="utf-8">
<title>Morvane Equity LLC – Business Card</title>
<link href="https://fonts.googleapis.com/css2?family=Archivo+Black&family=Arimo:wght@400;700&display=swap" rel="stylesheet">
<style>
  :root {
    --navy: #12416f;
    --grey-text: #8c8c8c;
    --grey-mark: #9a9a9a;
    --faint: #ecebf2;
    --card: #ffffff;
    --backdrop: #e6e6e6;
  }
  * { margin: 0; padding: 0; box-sizing: border-box; }
  html, body { width: 1200px; height: 1200px; overflow: hidden; background: var(--backdrop); }
  .sheet {
    width: 1200px; height: 1200px;
    display: flex; flex-direction: column; align-items: center; justify-content: center;
    gap: 22px;
  }
  .card {
    position: relative; width: 960px; height: 549px;
    background: var(--card); overflow: hidden;
    box-shadow: 0 4px 14px rgba(0,0,0,0.12);
  }
  .band { position: absolute; top: 0; background: var(--navy); }
  .brand-dot { position: absolute; border-radius: 50%; background: var(--navy); border: 10px solid var(--card); }
  .company-name {
    position: absolute; font-family: "Archivo Black", "Arial Black", sans-serif;
    color: var(--navy); white-space: nowrap; transform: translateX(-50%);
  }

  /* front */
  .card--front .band { left: 450px; width: 166px; height: 112px; }
  .card--front .brand-dot { left: 458px; top: 108px; width: 150px; height: 150px; }
  .card--front .company-name { left: 533px; top: 282px; font-size: 30px; }

  /* back */
  .faint-disc { position: absolute; left: 60px; top: -10px; width: 420px; height: 420px; border-radius: 50%; background: var(--faint); }
  .card--back .band { left: 685px; width: 166px; height: 92px; }
  .card--back .brand-dot { left: 688px; top: 82px; width: 160px; height: 160px; }
  .card--back .company-name { left: 768px; top: 262px; font-size: 34px; }
  .side-bar { position: absolute; left: 0; top: 335px; width: 46px; height: 112px; background: var(--navy); }
  .holder { position: absolute; left: 120px; top: 338px; font-family: "Arimo", Arial, sans-serif; }
  .holder-name { font-family: "Archivo Black", "Arial Black", sans-serif; font-size: 30px; color: var(--navy); line-height: 1; }
  .holder-title { font-size: 22px; color: var(--grey-text); margin-top: 2px; }
  .contact { list-style: none; margin-top: 18px; font-size: 22px; color: var(--grey-text); }
  .contact li { display: flex; align-items: center; gap: 10px; height: 32px; white-space: nowrap; }
  .contact svg { width: 16px; height: 20px; flex: none; }
</style>
</head>
<body>
<main class="sheet">
  <section class="card card--front" aria-label="Card front">
    <div class="band"></div>
    <div class="brand-dot"></div>
    <div class="company-name">Morvane Equity LLC</div>
  </section>

  <section class="card card--back" aria-label="Card back">
    <div class="faint-disc"></div>
    <div class="band"></div>
    <div class="brand-dot"></div>
    <div class="company-name">Morvane Equity LLC</div>
    <div class="side-bar"></div>
    <div class="holder">
      <p class="holder-name">Peter Dalby</p>
      <p class="holder-title">Portfolio Manager</p>
      <ul class="contact">
        <li>
          <svg viewBox="0 0 16 20" aria-hidden="true"><rect x="2" y="1" width="12" height="18" rx="2" fill="none" stroke="var(--navy)" stroke-width="2"/><line x1="6" y1="16" x2="10" y2="16" stroke="var(--navy)" stroke-width="1.5"/></svg>
          (412) 555-0187
        </li>
        <li>
          <svg viewBox="0 0 16 20" aria-hidden="true"><path d="M8 19 C3 12 1.5 9.5 1.5 7 A6.5 6.5 0 0 1 14.5 7 C14.5 9.5 13 12 8 19 Z" fill="none" stroke="var(--navy)" stroke-width="2"/><circle cx="8" cy="7" r="2.2" fill="var(--navy)"/></svg>
          2650 Birchmont Lane, Suite 300, Atlanta GA 30327
        </li>
      </ul>
    </div>
  </section>
</main>
</body>
</html>
```